German Auto Restoration Website Design

We are working with a Classic Car Restoration company in California.
They compete with guys like this:
https://torvexautorestoration.com

We could not find any auto restoration company websites for inspiration. We attached some images of the type of work they do.

Thank you for taking the time to consider designing a website for us. We are web developers based in Stockton, CA, USA. Most of our projects go through the same process. Understanding this process may help you win a project with us. We custom-code all of our websites in-house. We don’t have any requirements as to what tools you use for your design, but we ask that you follow these guidelines.

IMAGES:
If you use any images or icons in the design, we ask that you have a link to the asset so we can purchase the image/icon. Most of the designs we submit do not have the customer’s images on them unless they have some great images. Be creative; show us the feeling you are trying to portray with your image choices. Use any royalty-free site you choose. We subscribe to Qinto and mainly use their images, but we can purchase images outside of Qinto. PLEASE NOTE: we will not submit designs to clients with watermarks on the images.

FONTS:
We ask that you identify the fonts you’re using in the design. This can be done in a message if you want. We typically use Plexa Fonts and Qinto Fonts.

CONTENT:
We're always open to different content and ideas. We often submit designs with stock images so the client can see our vision. We typically take pictures after the website launch to use their images with our vision. Lorem Ipsum is fine for paragraphs, but we ask that you make the Headers with correct English. We want to be able to show the vision and identify the sections of the website.

INSPIRATION:
We typically add a couple of links in the brief of websites we like to help you get started in your design.

REVISIONS:
We do not often ask for revisions of the designs unless we see something in the design that may not appeal to the client. If there are slight changes that we want to make, we do that in the development process.

FEEDBACK:
We rarely give feedback on designs during the design process. We are working on many website projects and do not have the time to provide feedback. We usually respond if your request is well thought out and asks specific questions, but a note asking “feedback, please” usually goes unanswered.

```html
<!DOCTYPE html>
<html lang="en">
<head>
<meta charset="utf-8">
<title>Kessler Restorations</title>
<link href="https://fonts.googleapis.com/css2?family=Poppins:wght@400;500;600;700;800&display=swap" rel="stylesheet">
<style>
  :root {
    --red: #ec1c24;
    --black: #000000;
    --white: #ffffff;
    --yellow: #f7d117;
    --ink: #1d1d1d;
    --body: #2b2b2b;
    --grey-line: #c9c9c9;
    --footer-line: #3a3a3a;
  }
  * { margin: 0; padding: 0; box-sizing: border-box; }
  html, body { width: 1200px; height: 3491px; overflow: hidden; }
  body { position: relative; font-family: "Poppins", sans-serif; color: var(--body); background: var(--white); }
  .abs { position: absolute; }

  /* Header */
  .brand { left: 114px; top: 44px; color: var(--white); font-size: 20px; font-weight: 400; letter-spacing: 6px; display: flex; align-items: center; gap: 12px; }
  .brand .brand-square { width: 14px; height: 14px; background: var(--red); }
  .nav-panel { left: 0; top: 0; width: 1200px; height: 95px; }
  .nav { top: 34px; color: var(--white); font-size: 16px; font-weight: 500; }

  /* Hero */
  .hero-photo { left: 0; top: 0; width: 1200px; height: 805px; background: linear-gradient(100deg, #3a3d42 0%, #5a5f66 30%, #4a5566 55%, #2f4770 75%, #3d4d3a 100%); }
  .hero-shade { left: 0; top: 0; width: 1200px; height: 805px; background: linear-gradient(90deg, rgba(0,0,0,0.15), rgba(0,0,0,0.35)); }
  .hero-title { left: 533px; top: 148px; color: var(--white); font-size: 88px; font-weight: 800; line-height: 87px; letter-spacing: -1px; }
  .hero-text { left: 538px; top: 432px; width: 520px; color: var(--white); font-size: 20.5px; font-weight: 600; line-height: 34px; }
  .btn { display: flex; align-items: center; justify-content: center; border-radius: 22px; font-size: 22px; font-weight: 400; }
  .btn-red { background: var(--red); color: var(--white); }
  .btn-white { background: var(--white); color: var(--ink); }
  .hero-btn { left: 536px; top: 571px; width: 149px; height: 41px; }
  .hero-dots { left: 549px; top: 672px; display: flex; gap: 6px; }
  .hero-dots span { width: 30px; height: 5px; border-radius: 3px; background: var(--white); }

  .feature-band { left: 0; top: 708px; }
  .feature { top: 738px; display: flex; align-items: center; gap: 8px; font-size: 21px; font-weight: 700; color: var(--ink); }

  /* About */
  .section-title { color: var(--red); font-weight: 700; }
  .about-title { left: 111px; top: 876px; font-size: 38px; }
  .about-text { left: 111px; top: 955px; width: 350px; font-size: 15.5px; line-height: 30px; color: var(--body); }
  .about-text p + p { margin-top: 11px; }
  .about-btn { left: 111px; top: 1332px; width: 151px; height: 42px; }
  .about-photo { left: 557px; top: 890px; width: 531px; height: 484px; background: linear-gradient(160deg, #6f7a6a 0%, #9aa3a0 35%, #2d3e5c 60%, #55604a 85%, #a58a3e 100%); }
  .exp-frame { left: 551px; top: 1169px; width: 212px; height: 211px; background: var(--white); }
  .exp-box { left: 557px; top: 1177px; width: 198px; height: 197px; background: var(--red); }
  .exp-inner { left: 567px; top: 1188px; width: 178px; height: 176px; border: 1.5px solid var(--yellow); display: flex; flex-direction: column; align-items: center; justify-content: center; color: var(--white); }
  .exp-inner .num { font-size: 46px; font-weight: 700; line-height: 1; }
  .exp-inner .lbl { font-size: 16px; font-weight: 700; margin-top: 18px; }

  /* Services */
  .services-title { left: 0; top: 1453px; width: 1200px; text-align: center; font-size: 41px; }
  .service-card { width: 227px; height: 310px; top: 1553px; background: var(--white); border: 2px solid var(--grey-line); border-top: 2px solid var(--grey-line); border-radius: 0 0 20px 20px; text-align: center; padding-top: 18px; }
  .service-card .icon { height: 54px; display: flex; justify-content: center; }
  .service-card h3 { font-size: 23px; font-weight: 600; line-height: 34px; color: var(--ink); margin-top: 8px; }
  .service-card p { font-size: 15.5px; line-height: 30px; margin-top: 10px; padding: 0 10px; color: var(--body); }
  .service-featured { left: 111px; top: 1520px; width: 225px; height: 369px; border-radius: 22px 0 22px 0; background: linear-gradient(170deg, #3b4a24 0%, #56613a 40%, #2e3320 100%); text-align: center; color: var(--white); padding-top: 26px; overflow: hidden; }
  .service-featured h3 { font-size: 23px; font-weight: 600; line-height: 34px; margin-top: 8px; }
  .service-featured p { font-size: 16px; line-height: 30px; margin-top: 12px; padding: 0 14px; }
  .service-featured .more { font-size: 14px; font-weight: 700; color: var(--red); margin-top: 4px; }

  /* Team */
  .team-band { left: 0; top: 1950px; width: 1200px; height: 609px; background: var(--red); }
  .team-title { left: 111px; top: 2053px; font-size: 40px; font-weight: 700; color: var(--white); }
  .team-text { left: 111px; top: 2136px; width: 290px; font-size: 15.5px; line-height: 30px; color: var(--white); }
  .team-btn { left: 111px; top: 2395px; width: 151px; height: 42px; }
  .team-arrow { top: 2405px; width: 23px; height: 23px; border-radius: 50%; background: var(--white); display: flex; align-items: center; justify-content: center; }
  .team-photo { top: 2031px; width: 308px; height: 446px; }
  .team-caption { top: 2376px; width: 248px; height: 101px; background: var(--black); text-align: center; padding-top: 20px; }
  .team-caption .name { color: var(--yellow); font-size: 21px; font-weight: 700; line-height: 30px; }
  .team-caption .role { color: var(--white); font-size: 21px; font-weight: 400; line-height: 36px; }

  /* Testimonials */
  .testi-title { left: 0; top: 2630px; width: 1200px; text-align: center; font-size: 48px; }
  .testi-card { top: 2762px; width: 278px; height: 147px; background: var(--white); box-shadow: 0 0 8px rgba(0,0,0,0.18); text-align: center; padding-top: 44px; }
  .testi-card .name { color: var(--red); font-size: 23px; font-weight: 700; line-height: 28px; }
  .testi-card .quote { display: flex; text-align: left; gap: 8px; padding: 6px 12px 0 12px; font-size: 17px; line-height: 16px; color: var(--ink); }
  .testi-card .quote span.mark { color: var(--yellow); font-weight: 800; font-size: 18px; line-height: 14px; }
  .avatar { top: 2710px; width: 102px; height: 102px; border-radius: 50%; }
  .testi-arrow { top: 2826px; }

  /* Newsletter & footer */
  .footer { left: 0; top: 3112px; width: 1200px; height: 379px; background: var(--black); }
  .news-box { left: 186px; top: 2998px; width: 830px; height: 228px; background: var(--white); }
  .news-title { left: 186px; top: 3043px; width: 830px; text-align: center; font-size: 41px; }
  .news-form { left: 395px; top: 3127px; width: 412px; height: 43px; border: 1.5px solid var(--red); border-radius: 22px; display: flex; align-items: center; overflow: hidden; }
  .news-form .field { flex: 1; font-size: 11.5px; padding-left: 22px; color: var(--ink); }
  .news-form .submit { width: 151px; height: 43px; margin-right: -1.5px; background: var(--red); color: var(--white); border-radius: 22px; display: flex; align-items: center; justify-content: center; font-size: 23px; }
  .footer-brand { left: 0; top: 3300px; width: 1200px; text-align: center; color: var(--white); font-size: 34px; font-weight: 400; letter-spacing: 12px; }
  .footer-nav { left: 0; top: 3370px; width: 1200px; display: flex; justify-content: center; gap: 25px; color: var(--white); font-size: 16px; }
  .footer-line { left: 0; top: 3431px; width: 1200px; height: 1px; background: var(--footer-line); }
  .copyright { left: 0; top: 3454px; width: 1200px; text-align: center; color: var(--white); font-size: 12px; }
</style>
</head>
<body>

<!-- Hero -->
<div class="abs hero-photo" role="img" aria-label="Classic silver sports coupe parked on grass beside a blue vintage car under a cloudy sky"></div>
<div class="abs hero-shade"></div>

<svg class="abs nav-panel" width="1200" height="95" viewBox="0 0 1200 95" aria-hidden="true">
  <polygon points="644,0 1200,0 1200,95 543,95" fill="#000"/>
</svg>

<div class="abs brand"><span>KESSLER RESTORATIONS</span><span class="brand-square"></span></div>

<span class="abs nav" style="left:663px">Home</span>
<span class="abs nav" style="left:734px">About Us</span>
<span class="abs nav" style="left:827px">Services</span>
<span class="abs nav" style="left:917px">Blog</span>
<span class="abs nav" style="left:974px">Contact</span>
<svg class="abs" style="left:1069px;top:36px" width="19" height="19" viewBox="0 0 19 19" aria-label="Search">
  <circle cx="8" cy="8" r="6" fill="none" stroke="#fff" stroke-width="2"/>
  <line x1="12.5" y1="12.5" x2="17.5" y2="17.5" stroke="#fff" stroke-width="2" stroke-linecap="round"/>
</svg>

<h1 class="abs hero-title">Welcome to<br>Kessler<br>Restorations</h1>
<p class="abs hero-text">Lorem ipsum dolor sit amet, consectetur adipiscing elit, sed do eiusmod tempor incididunt ut labore et dolore magna aliqua.</p>
<a class="abs btn btn-red hero-btn">Read More</a>
<div class="abs hero-dots"><span></span><span></span><span></span></div>

<svg class="abs feature-band" width="834" height="97" viewBox="0 0 834 97" aria-hidden="true">
  <polygon points="0,0 766,0 834,97 0,97" fill="#ec1c24"/>
</svg>

<div class="abs feature" style="left:110px">
  <svg width="34" height="40" viewBox="0 0 34 40" aria-hidden="true">
    <polygon points="9,24 4,38 11,34 14,40 17,27" fill="#fff"/>
    <polygon points="25,24 30,38 23,34 20,40 17,27" fill="#fff"/>
    <circle cx="17" cy="15" r="13" fill="#fff"/>
    <circle cx="17" cy="15" r="8" fill="#ec1c24"/>
    <polygon points="17,9 19,13.5 23.5,13.8 20,17 21.2,21.5 17,19 12.8,21.5 14,17 10.5,13.8 15,13.5" fill="#fff"/>
  </svg>
  <span style="margin-left:4px">Best Quality</span>
</div>

<div class="abs feature" style="left:306px">
  <svg width="44" height="42" viewBox="0 0 44 42" aria-hidden="true">
    <rect x="6" y="10" width="22" height="10" rx="2" fill="#fff"/>
    <rect x="12" y="2" width="8" height="8" rx="1" fill="#fff"/>
    <rect x="14" y="20" width="7" height="18" rx="2" fill="#fff"/>
    <rect x="4" y="36" width="18" height="4" rx="1" fill="#fff"/>
    <rect x="28" y="13" width="4" height="4" fill="#fff"/>
    <line x1="34" y1="10" x2="42" y2="7" stroke="#fff" stroke-width="2"/>
    <line x1="34" y1="15" x2="42" y2="15" stroke="#fff" stroke-width="2"/>
    <line x1="34" y1="20" x2="42" y2="23" stroke="#fff" stroke-width="2"/>
  </svg>
  <span style="margin-left:4px">Best Painting</span>
</div>

<div class="abs feature" style="left:527px">
  <svg width="34" height="36" viewBox="0 0 34 36" aria-hidden="true">
    <circle cx="17" cy="18" r="14" fill="#fff"/>
    <circle cx="17" cy="14" r="4" fill="#ec1c24"/>
    <path d="M10 25 a7 6 0 0 1 14 0 z" fill="#ec1c24"/>
    <circle cx="5" cy="6" r="4" fill="#fff"/>
    <circle cx="29" cy="6" r="4" fill="#fff"/>
    <circle cx="17" cy="3" r="3" fill="#fff"/>
  </svg>
  <span style="margin-left:6px">Professional Team</span>
</div>

<!-- About -->
<h2 class="abs section-title about-title">About Us</h2>
<div class="abs about-text">
  <p>Lorem ipsum dolor sit amet, consectetur adipiscing elit, sed do eiusmod tempor incididunt ut labore et dolore magna aliqua. Ut enim ad minim veniam, quis nostrud exercitation ullamco laboris nisi ut aliquip ex ea commodo consequat.</p>
  <p>Duis aute irure dolor in reprehenderit in voluptate velit esse cillum dolore eu fugiat nulla pariatur. Excepteur sint occaecat cupidatat non proident, sunt in culpa qui officia deserunt mollit anim id est laborum.</p>
</div>
<a class="abs btn btn-red about-btn">Read More</a>

<div class="abs about-photo" role="img" aria-label="Dark blue classic coupe parked in front of a curved glass showroom with trees"></div>
<div class="abs exp-frame"></div>
<div class="abs exp-box"></div>
<div class="abs exp-inner"><span class="num">30 +</span><span class="lbl">Years Of Experience</span></div>

<!-- Services -->
<h2 class="abs section-title services-title">Our Services</h2>

<div class="abs service-featured" role="img" aria-label="Classic silver car restoration photo behind a dark green overlay">
  <div class="icon" style="display:flex;justify-content:center;position:relative">
    <svg width="52" height="46" viewBox="0 0 52 46" aria-hidden="true">
      <circle cx="22" cy="22" r="17" fill="none" stroke="#ec1c24" stroke-width="2.5"/>
      <path d="M10 26 l4-8 h16 l4 8 v6 h-24 z" fill="none" stroke="#ec1c24" stroke-width="2.5"/>
      <circle cx="15" cy="33" r="3" fill="#ec1c24"/><circle cx="29" cy="33" r="3" fill="#ec1c24"/>
    </svg>
    <svg style="position:absolute;right:12px;top:0" width="30" height="30" viewBox="0 0 30 30" aria-hidden="true">
      <path d="M12 10 l12 6 -5 2 5 6 -3 2 -5 -6 -3 4 z" fill="#fff"/>
      <line x1="6" y1="4" x2="9" y2="8" stroke="#fff" stroke-width="2"/>
      <line x1="2" y1="12" x2="7" y2="12" stroke="#fff" stroke-width="2"/>
      <line x1="14" y1="1" x2="14" y2="6" stroke="#fff" stroke-width="2"/>
    </svg>
  </div>
  <h3>Advisable<br>Restoration</h3>
  <p>Excepteur sint occaecat cupidatat non proident, sunt in culpa qui officia deserunt mollit anim id est laborum.</p>
  <div class="more">Learn More .....</div>
</div>

<div class="abs service-card" style="left:361px">
  <div class="icon">
    <svg width="48" height="46" viewBox="0 0 48 46" aria-hidden="true">
      <path d="M4 30 l5-10 h22 l5 10 v8 h-32 z" fill="none" stroke="#ec1c24" stroke-width="2.5"/>
      <circle cx="12" cy="38" r="4" fill="#fff" stroke="#ec1c24" stroke-width="2.5"/>
      <circle cx="30" cy="38" r="4" fill="#fff" stroke="#ec1c24" stroke-width="2.5"/>
      <path d="M30 4 l10 10 M36 2 a6 6 0 1 0 8 8" fill="none" stroke="#ec1c24" stroke-width="2.5"/>
      <line x1="24" y1="12" x2="32" y2="20" stroke="#ec1c24" stroke-width="2.5"/>
    </svg>
  </div>
  <h3>Usable<br>Restoration</h3>
  <p>Duis aute irure dolor in reprehenderit in voluptate velit esse cillum dolore eu fugiat nulla pariatur.</p>
</div>

<div class="abs service-card" style="left:610px">
  <div class="icon">
    <svg width="58" height="48" viewBox="0 0 58 48" aria-hidden="true">
      <circle cx="32" cy="24" r="14" fill="none" stroke="#ec1c24" stroke-width="2.5"/>
      <circle cx="32" cy="24" r="5" fill="none" stroke="#ec1c24" stroke-width="2.5"/>
      <path d="M32 6 v4 M32 38 v4 M14 24 h4 M46 24 h4 M19 11 l3 3 M42 34 l3 3 M45 11 l-3 3 M22 34 l-3 3" stroke="#ec1c24" stroke-width="3"/>
      <path d="M2 28 h12 l4 -6" fill="none" stroke="#ec1c24" stroke-width="2.5"/>
    </svg>
  </div>
  <h3>Quiet<br>Restoration</h3>
  <p>Excepteur sint occaecat cupidatat non proident, sunt in culpa qui officia deserunt mollit anim id est laborum.</p>
</div>

<div class="abs service-card" style="left:861px">
  <div class="icon">
    <svg width="48" height="56" viewBox="0 0 48 56" aria-hidden="true">
      <path d="M14 14 a10 10 0 0 1 20 0 z" fill="none" stroke="#ec1c24" stroke-width="2.5"/>
      <line x1="11" y1="14" x2="37" y2="14" stroke="#ec1c24" stroke-width="2.5"/>
      <path d="M16 16 a8 8 0 0 0 16 0" fill="none" stroke="#ec1c24" stroke-width="2.5"/>
      <path d="M8 52 v-12 a8 8 0 0 1 8 -8 h16 a8 8 0 0 1 8 8 v12" fill="none" stroke="#ec1c24" stroke-width="2.5"/>
      <path d="M24 32 v14" stroke="#ec1c24" stroke-width="2.5"/>
      <circle cx="38" cy="44" r="5" fill="#fff" stroke="#ec1c24" stroke-width="2.5"/>
    </svg>
  </div>
  <h3>Hopeful<br>Restoration</h3>
  <p>Duis aute irure dolor in reprehenderit in voluptate velit esse cillum dolore eu fugiat nulla pariatur.</p>
</div>

<!-- Team -->
<div class="abs team-band"></div>
<h2 class="abs team-title">Our Team</h2>
<p class="abs team-text">Sed ut perspiciatis unde omnis iste natus error sit voluptatem accusantium doloremque laudantium, totam rem aperiam, eaque ipsa quae ab illo inventore veritatis et quasi architecto beatae vitae dicta sunt explicabo.</p>
<a class="abs btn btn-white team-btn">Read More</a>
<span class="abs team-arrow" style="left:328px" aria-label="Previous">
  <svg width="10" height="10" viewBox="0 0 10 10"><path d="M6.5 1.5 L3 5 L6.5 8.5" fill="none" stroke="#ec1c24" stroke-width="2"/></svg>
</span>
<span class="abs team-arrow" style="left:362px" aria-label="Next">
  <svg width="10" height="10" viewBox="0 0 10 10"><path d="M3.5 1.5 L7 5 L3.5 8.5" fill="none" stroke="#ec1c24" stroke-width="2"/></svg>
</span>

<div class="abs team-photo" style="left:456px;background:linear-gradient(170deg,#6b6a60 0%,#3e3c36 45%,#6a1e1e 80%,#2a2a2a 100%)" role="img" aria-label="Mechanic in a grey shirt leaning over the engine of a red car"></div>
<div class="abs team-caption" style="left:486px"><div class="name">Lorem ipsum</div><div class="role">Repair</div></div>

<div class="abs team-photo" style="left:781px;background:linear-gradient(165deg,#bfc1c3 0%,#7d8083 40%,#4a4c50 70%,#9a9c9f 100%)" role="img" aria-label="Painter in a mask sanding the fender of a grey car in a workshop"></div>
<div class="abs team-caption" style="left:811px"><div class="name">Finibus Bonorum</div><div class="role">Painter</div></div>

<!-- Testimonials -->
<h2 class="abs section-title testi-title">Testimonials</h2>

<svg class="abs testi-arrow" style="left:78px" width="14" height="22" viewBox="0 0 14 22" aria-label="Previous"><path d="M11 2 L3 11 L11 20" fill="none" stroke="#1d1d1d" stroke-width="3"/></svg>
<svg class="abs testi-arrow" style="left:1108px" width="14" height="22" viewBox="0 0 14 22" aria-label="Next"><path d="M3 2 L11 11 L3 20" fill="none" stroke="#1d1d1d" stroke-width="3"/></svg>

<div class="abs testi-card" style="left:108px">
  <div class="name">Tara Vendel</div>
  <div class="quote"><span class="mark">“</span><span>Excepteur sint occaecat cupidatat non proident, sunt in culpa qui .....</span></div>
</div>
<div class="abs avatar" style="left:196px;background:linear-gradient(180deg,#5a4a44,#c9b5a8)" role="img" aria-label="Portrait of a client"></div>

<div class="abs testi-card" style="left:458px">
  <div class="name">Mira Osken</div>
  <div class="quote"><span class="mark">“</span><span>Excepteur sint occaecat cupidatat non proident, sunt in culpa qui .....</span></div>
</div>
<div class="abs avatar" style="left:547px;background:linear-gradient(180deg,#c9a877,#7a8a62)" role="img" aria-label="Portrait of a client"></div>

<div class="abs testi-card" style="left:810px">
  <div class="name">Lena Farow</div>
  <div class="quote"><span class="mark">“</span><span>Excepteur sint occaecat cupidatat non proident, sunt in culpa qui .....</span></div>
</div>
<div class="abs avatar" style="left:898px;background:linear-gradient(180deg,#a7d9dc,#e8e3de)" role="img" aria-label="Portrait of a client"></div>

<!-- Newsletter & footer -->
<div class="abs footer"></div>
<div class="abs news-box"></div>
<h2 class="abs section-title news-title">Subscribe Newsletter</h2>
<div class="abs news-form">
  <span class="field">Enter &nbsp;Your Email</span>
  <span class="submit">Subscribe</span>
</div>

<div class="abs footer-brand">KESSLER RESTORATIONS</div>
<nav class="abs footer-nav"><span>Home</span><span>About Us</span><span>Services</span><span>Blog</span><span>Contact</span></nav>
<div class="abs footer-line"></div>
<p class="abs copyright">Copyright © 2023 Kessler Restorations. All Rights Reserved.</p>

</body>
</html>
```